Business Card Design for a Lending Business (Hard Money loans)

We need a business card for our Real Estate Lending business. We do hard Money loans for real estate investors. We have an existing logo we like, see attached. I'd like the business card to mostly include the logo colors, but a bright color pop of some sort would be nice to see also. Card should include Logo, Company Name, Company Address, Employee Name, Cell Phone, Main Phone, Email, Website

Industry/Entity Type

Finance / Lending

Contact Information for Business Card

Logo, Company Name, Company Address, Employee Name, Cell Phone, Main Phone, Email, Website

Requirements
Nice to have
• I'd like the business card to mostly include the logo colors, but a bright color pop of some sort would be nice to see also.

```html
<!DOCTYPE html>
<html lang="en">
<head>
<meta charset="utf-8">
<title>Crestway Lending – Business Card</title>
<link rel="stylesheet" href="https://fonts.googleapis.com/css2?family=Lato:wght@300;400;700&display=swap">
<style>
  :root {
    --navy: #283a85;
    --sky: #10ace0;
    --white: #ffffff;
    --page: #eeeeef;
    --shadow: rgba(0, 0, 0, 0.28);
  }
  * { margin: 0; padding: 0; box-sizing: border-box; }
  html, body { width: 1200px; height: 1200px; overflow: hidden; }
  body {
    background: var(--page);
    font-family: "Lato", sans-serif;
    position: relative;
  }
  .card {
    position: absolute;
    left: 171px;
    width: 858px;
    height: 503px;
    background: var(--white);
    box-shadow: 0 6px 14px var(--shadow);
    overflow: hidden;
  }
  .card--front { top: 66px; }
  .card--back { top: 631px; }
  .card__shapes { position: absolute; inset: 0; width: 100%; height: 100%; }

  .brand {
    position: absolute;
    display: flex;
    flex-direction: column;
    align-items: center;
    color: var(--navy);
    font-weight: 400;
    text-align: center;
  }
  .brand__dot { border-radius: 50%; background: var(--navy); }
  .brand__name { letter-spacing: 0.18em; line-height: 1.25; text-transform: uppercase; }

  .card--front .brand { left: 60px; top: 80px; width: 260px; }
  .card--front .brand__dot { width: 70px; height: 70px; margin-bottom: 18px; }
  .card--front .brand__name { font-size: 30px; }

  .card--back .brand { left: 229px; top: 120px; width: 400px; }
  .card--back .brand__dot { width: 110px; height: 110px; margin-bottom: 26px; }
  .card--back .brand__name { font-size: 46px; }

  .holder {
    position: absolute;
    right: 57px;
    top: 228px;
    color: var(--white);
    font-weight: 700;
    font-size: 33px;
  }
  .contacts {
    position: absolute;
    right: 26px;
    top: 316px;
    list-style: none;
    color: var(--white);
    font-weight: 300;
    font-size: 20px;
  }
  .contacts li {
    display: flex;
    align-items: center;
    justify-content: flex-end;
    height: 36.5px;
  }
  .contacts svg { width: 16px; height: 16px; margin-left: 14px; flex: none; }

  .address {
    position: absolute;
    left: 184px;
    top: 394px;
    display: flex;
    align-items: flex-start;
    color: var(--white);
    font-weight: 300;
    font-size: 20px;
    line-height: 28px;
  }
  .address svg { width: 14px; height: 18px; margin: 4px 10px 0 0; }
</style>
</head>
<body>

<section class="card card--front" aria-label="Business card front">
  <svg class="card__shapes" viewBox="0 0 686 402" preserveAspectRatio="none" aria-hidden="true">
    <polygon points="686,0 686,402 173,402 79,357" fill="var(--sky)"/>
    <polygon points="0,320 0,402 173,402" fill="var(--navy)"/>
    <polygon points="420,0 635,0 541,54" fill="var(--navy)"/>
  </svg>

  <div class="brand">
    <span class="brand__dot"></span>
    <span class="brand__name">Crestway<br>Lending</span>
  </div>

  <h1 class="holder">Marten Vosselaer</h1>

  <ul class="contacts">
    <li>+00 9274 0000000
      <svg viewBox="0 0 16 16"><path d="M4 1.5l2.2 3-1.4 1.6c.8 2 2.3 3.5 4.3 4.3l1.6-1.4 3 2.2-1.4 2.8C6.5 14 2 9.5 1.5 3.2z" fill="var(--white)"/></svg>
    </li>
    <li>+001628 0000000
      <svg viewBox="0 0 16 16"><rect x="4.5" y="1" width="7" height="14" rx="1.3" fill="none" stroke="var(--white)" stroke-width="1.2"/><circle cx="8" cy="12.8" r="0.8" fill="var(--white)"/></svg>
    </li>
    <li>marten@crestway-lending.co
      <svg viewBox="0 0 16 16"><rect x="2" y="4" width="12" height="8.5" fill="var(--white)"/><path d="M2 4l6 4.6L14 4" fill="none" stroke="var(--sky)" stroke-width="1.1"/></svg>
    </li>
    <li>www.crestway-lending.co
      <svg viewBox="0 0 16 16"><circle cx="8" cy="8" r="6.3" fill="var(--white)"/><path d="M1.7 8h12.6M8 1.7c-2.6 3.6-2.6 9 0 12.6M8 1.7c2.6 3.6 2.6 9 0 12.6" fill="none" stroke="var(--sky)" stroke-width="0.9"/></svg>
    </li>
  </ul>

  <address class="address">
    <svg viewBox="0 0 14 18"><path d="M7 1a5.5 5.5 0 0 0-5.5 5.5C1.5 10.5 7 17 7 17s5.5-6.5 5.5-10.5A5.5 5.5 0 0 0 7 1z" fill="var(--white)"/><circle cx="7" cy="6.5" r="2" fill="var(--sky)"/></svg>
    <span>Lindenweg 000<br>00000 Eichstadt</span>
  </address>
</section>

<section class="card card--back" aria-label="Business card back">
  <svg class="card__shapes" viewBox="0 0 686 402" preserveAspectRatio="none" aria-hidden="true">
    <polygon points="0,27 88,181 0,375" fill="var(--sky)"/>
    <polygon points="686,30 599,222 686,372" fill="var(--navy)"/>
  </svg>

  <div class="brand">
    <span class="brand__dot"></span>
    <span class="brand__name">Crestway<br>Lending</span>
  </div>
</section>

</body>
</html>
```